Quillbrook Health needs a new services brochure

We need a new brochure that highlights the services that we offer at our clinic. We are a multidisciplinary health clinic that focuses on injury rehabilitation and pain management. We are looking for a brochure that will highlight our primary services to our clientele and inform potential clients of what we can offer. We pride ourselves on our quality of care and our advanced treatment techniques.
Target Market(s)
young families, athletes, people interested in their health.
Industry/Entity Type
Health And Wellness
Colors
Designer to choose colors to be used in the design.
Requirements
Must have
- We would love our new brochure to be a tri-fold that has 6 pages. We would like it to have brief information about our featured services:
- - Chiropractic
- - Massage Therapy
- - Manual Osteopathic Therapy
- - Acupuncture
- - Laser Therapy
- - Radial Shockwave Therapy
- We would also like this brochure to include a brief price list and direct billing info, About Us section & Contact information.
Nice to have
- If there is space to list that we also offer other services such as : Tissue Unwind Method, Hot Stone Massage, Cupping Technique, Pembrill Method, and Kinesiology Taping that would be great. We would like to use images similar to those that are on our website (we have hi-res of all images on the website) www.quillbrookhealth.ca and colours that would fit with our logo.

```html
<!DOCTYPE html>
<html lang="en">
<head>
<meta charset="utf-8">
<title>Quillbrook Health – Services Brochure</title>
<link href="https://fonts.googleapis.com/css2?family=Open+Sans:wght@400;600;700;800&family=Montserrat:wght@600;700;800&display=swap" rel="stylesheet">
<style>
:root{
  --bg:#d9d9d9;
  --paper:#ffffff;
  --blue:#1f6fb8;
  --blue-dark:#0f4f8e;
  --blue-light:#e6f0fa;
  --ink:#3b3b3b;
  --muted:#7a7a7a;
  --rule:#d4dde7;
  --photo-a:#b9c9a6;
  --photo-b:#c7d3df;
  --photo-c:#dfe5ec;
}
*{box-sizing:border-box;margin:0;padding:0}
html,body{width:822px;height:1200px;overflow:hidden;background:var(--bg);font-family:"Open Sans",Arial,sans-serif;color:var(--ink)}
.canvas{position:relative;width:822px;height:1200px}
.sheet{position:absolute;left:30px;width:762px;height:520px;background:var(--paper);display:flex;box-shadow:0 4px 10px rgba(0,0,0,.18)}
.sheet--outside{top:30px}
.sheet--inside{top:640px}
.panel{position:relative;width:254px;height:100%;overflow:hidden;border-right:1px solid #eef1f4}
.panel:last-child{border-right:none}
.photo{width:100%}
.band{background:var(--blue);color:#fff;font-family:"Montserrat",sans-serif;font-weight:700;font-size:9px;letter-spacing:1px;text-align:center;padding:6px 0}
.band--notch{position:relative}
.body{padding:10px 14px;font-size:6.2px;line-height:1.55;color:var(--ink)}
.body p{margin-bottom:7px}
.brand{display:flex;align-items:center;gap:7px;justify-content:center;padding-top:20px}
.brand__dot{width:18px;height:18px;border-radius:50%;background:var(--blue)}
.brand__name{font-family:"Montserrat",sans-serif;font-weight:700;font-size:17px;color:var(--blue-dark)}
.phone{display:flex;align-items:center;justify-content:center;gap:8px;margin-top:14px;font-family:"Montserrat",sans-serif;font-weight:700;font-size:17px;color:var(--ink)}
.phone__icon{width:20px;height:20px;border-radius:50%;background:var(--blue);display:flex;align-items:center;justify-content:center}
.contact-lines{text-align:center;font-size:6px;color:var(--muted);margin:8px 0 12px;line-height:1.6}
.hours{width:200px;margin:10px auto 0;border-collapse:collapse;font-size:6.5px}
.hours td{padding:3px 4px;border-bottom:1px solid var(--rule)}
.hours td:first-child{color:var(--ink);font-weight:600}
.hours td:first-child::before{content:"";display:inline-block;width:4px;height:4px;background:var(--blue);margin-right:6px;vertical-align:middle}
.hours td:last-child{text-align:right;color:var(--muted)}
.note{margin:14px 18px 0;background:var(--blue);color:#fff;font-size:6px;line-height:1.5;padding:8px 10px;display:flex;gap:8px;align-items:center}
.note__icon{flex:0 0 16px;height:16px;border-radius:50%;background:rgba(255,255,255,.25)}
.social{display:flex;gap:6px;justify-content:center;margin-top:12px}
.social span{width:12px;height:12px;border-radius:2px;background:var(--blue)}
.hero{position:absolute;left:0;right:0;top:292px;height:160px;background:var(--blue);color:#fff;padding:26px 20px 0}
.hero__big{font-family:"Montserrat",sans-serif;font-weight:800;font-size:30px;line-height:1}
.hero__small{font-family:"Open Sans",sans-serif;font-weight:400;font-size:26px;line-height:1.1;margin-left:44px}
.web{position:absolute;left:0;right:0;bottom:0;height:68px;display:flex;align-items:center;justify-content:center;font-size:7px;color:var(--blue-dark);font-weight:600}
.services-grid{display:grid;grid-template-columns:1fr 1fr;gap:7px 8px;padding:2px 14px}
.service{display:flex;align-items:center;gap:6px;font-size:6.5px;font-weight:600;color:var(--ink);line-height:1.2}
.service__thumb{flex:0 0 24px;height:24px;border-radius:50%;background:linear-gradient(135deg,var(--photo-b),#a7b8c8)}
.billing{background:var(--blue-light);padding:8px 12px}
.billing__list{display:grid;grid-template-columns:1fr 1fr;gap:4px 8px}
.billing__item{display:flex;align-items:center;gap:4px;font-size:5.8px;color:var(--ink);background:#fff;padding:3px 4px}
.billing__item svg{flex:0 0 7px}
.heading-sm{font-family:"Montserrat",sans-serif;font-weight:700;font-size:8px;color:var(--blue-dark);margin-bottom:3px}
.prices{padding:6px 14px 0}
.price-group{margin-bottom:6px}
.price-row{display:flex;justify-content:space-between;font-size:5.8px;color:var(--muted);border-bottom:1px dotted var(--rule);padding:1px 0}
.price-cols{display:grid;grid-template-columns:1fr 1fr;gap:0 10px}
</style>
</head>
<body>
<div class="canvas">

  <!-- Outside spread -->
  <section class="sheet sheet--outside">
    <div class="panel panel--about">
      <div class="photo" role="img" aria-label="Woman stretching outdoors in a sunny park" style="height:170px;background:linear-gradient(135deg,#e9e3b8,var(--photo-a) 55%,#7e9b6a)"></div>
      <div class="band">ABOUT US</div>
      <div class="body">
        <p>Quillbrook Health is a multidisciplinary clinic in Calgary focused on injury rehabilitation and pain management. Our team of chiropractors, massage therapists and osteopathic practitioners works together to help you recover faster and move better every day.</p>
        <p>We pride ourselves on quality of care and on advanced treatment techniques. Each visit begins with a careful assessment so your plan fits your body, your goals and your lifestyle.</p>
        <p>Whether you are an athlete, a busy parent or simply someone who wants to feel well, we offer caring, hands-on treatment in a bright and welcoming space. Book today and let us help you live life pain free.</p>
      </div>
    </div>

    <div class="panel panel--contact">
      <div class="brand"><span class="brand__dot"></span><span class="brand__name">Quillbrook Health</span></div>
      <div class="phone">
        <span class="phone__icon"><svg width="10" height="10" viewBox="0 0 24 24"><path fill="#fff" d="M6.6 10.8a15 15 0 0 0 6.6 6.6l2.2-2.2a1 1 0 0 1 1-.25 11.4 11.4 0 0 0 3.6.6 1 1 0 0 1 1 1V20a1 1 0 0 1-1 1A17 17 0 0 1 3 4a1 1 0 0 1 1-1h3.5a1 1 0 0 1 1 1c0 1.25.2 2.45.6 3.6a1 1 0 0 1-.25 1z"/></svg></span>
        (403) 555-0148
      </div>
      <div class="contact-lines">12 Larchmont Way NW, Calgary AB<br>hello@quillbrookhealth.ca</div>
      <div class="band">HOURS</div>
      <table class="hours">
        <tr><td>Monday</td><td>8am – 8pm</td></tr>
        <tr><td>Tuesday</td><td>8am – 8pm</td></tr>
        <tr><td>Wednesday</td><td>8am – 8pm</td></tr>
        <tr><td>Thursday</td><td>8am – 8pm</td></tr>
        <tr><td>Friday</td><td>8am – 6pm</td></tr>
        <tr><td>Saturday</td><td>9am – 4pm</td></tr>
        <tr><td>Sunday</td><td>Closed</td></tr>
      </table>
      <div class="note"><span class="note__icon"></span><span>New patients are always welcome. Evening and weekend visits are available by appointment.</span></div>
      <div class="social"><span></span><span></span><span></span><span></span></div>
    </div>

    <div class="panel panel--cover">
      <div class="photo" role="img" aria-label="Smiling team of clinic practitioners in white coats" style="height:292px;background:linear-gradient(160deg,#f2f5f8,var(--photo-b) 60%,#9fb2c6)"></div>
      <div class="hero">
        <div class="hero__big">LIVE LIFE</div>
        <div class="hero__small">pain free</div>
      </div>
      <div class="web">www.quillbrookhealth.ca</div>
    </div>
  </section>

  <!-- Inside spread -->
  <section class="sheet sheet--inside">
    <div class="panel panel--services">
      <div class="photo" role="img" aria-label="Practitioner shaking hands with a patient" style="height:120px;background:linear-gradient(135deg,var(--photo-c),#b7c7d8)"></div>
      <div class="band">SERVICES</div>
      <div class="body">
        <p>Our clinic offers a full range of treatments under one roof, so your care stays connected from first visit to full recovery. Ask our team which approach suits you best.</p>
      </div>
      <div class="services-grid">
        <div class="service"><span class="service__thumb" role="img" aria-label="Chiropractic treatment"></span>Chiropractic</div>
        <div class="service"><span class="service__thumb" role="img" aria-label="Massage therapy"></span>Massage Therapy</div>
        <div class="service"><span class="service__thumb" role="img" aria-label="Osteopathic therapy"></span>Manual Osteopathic Therapy</div>
        <div class="service"><span class="service__thumb" role="img" aria-label="Acupuncture needles"></span>Acupuncture</div>
        <div class="service"><span class="service__thumb" role="img" aria-label="Shockwave therapy"></span>Radial Shockwave Therapy</div>
        <div class="service"><span class="service__thumb" role="img" aria-label="Laser therapy"></span>Laser Therapy</div>
        <div class="service"><span class="service__thumb" role="img" aria-label="Cupping treatment"></span>Cupping Technique</div>
        <div class="service"><span class="service__thumb" role="img" aria-label="Hot stones on back"></span>Hot Stone Massage</div>
      </div>
    </div>

    <div class="panel panel--billing">
      <div class="band">WE DIRECT BILL</div>
      <div class="body" style="padding-bottom:6px"><p>We bill most insurance providers directly, so you pay only your share at the time of your visit.</p></div>
      <div class="billing">
        <div class="billing__list">
          <div class="billing__item"><svg width="7" height="7" viewBox="0 0 10 10"><path d="M1 5l3 3 5-6" stroke="#1f6fb8" stroke-width="1.8" fill="none"/></svg>Northvale Benefits</div>
          <div class="billing__item"><svg width="7" height="7" viewBox="0 0 10 10"><path d="M1 5l3 3 5-6" stroke="#1f6fb8" stroke-width="1.8" fill="none"/></svg>Harbourline Life</div>
          <div class="billing__item"><svg width="7" height="7" viewBox="0 0 10 10"><path d="M1 5l3 3 5-6" stroke="#1f6fb8" stroke-width="1.8" fill="none"/></svg>Cedarmark Insurance</div>
          <div class="billing__item"><svg width="7" height="7" viewBox="0 0 10 10"><path d="M1 5l3 3 5-6" stroke="#1f6fb8" stroke-width="1.8" fill="none"/></svg>Brightwell Group</div>
          <div class="billing__item"><svg width="7" height="7" viewBox="0 0 10 10"><path d="M1 5l3 3 5-6" stroke="#1f6fb8" stroke-width="1.8" fill="none"/></svg>Oakpath Health</div>
          <div class="billing__item"><svg width="7" height="7" viewBox="0 0 10 10"><path d="M1 5l3 3 5-6" stroke="#1f6fb8" stroke-width="1.8" fill="none"/></svg>Summitreach Plans</div>
          <div class="billing__item"><svg width="7" height="7" viewBox="0 0 10 10"><path d="M1 5l3 3 5-6" stroke="#1f6fb8" stroke-width="1.8" fill="none"/></svg>Tallgrass Mutual</div>
          <div class="billing__item"><svg width="7" height="7" viewBox="0 0 10 10"><path d="M1 5l3 3 5-6" stroke="#1f6fb8" stroke-width="1.8" fill="none"/></svg>Riverstone Care</div>
          <div class="billing__item"><svg width="7" height="7" viewBox="0 0 10 10"><path d="M1 5l3 3 5-6" stroke="#1f6fb8" stroke-width="1.8" fill="none"/></svg>Westfall Assurance</div>
          <div class="billing__item"><svg width="7" height="7" viewBox="0 0 10 10"><path d="M1 5l3 3 5-6" stroke="#1f6fb8" stroke-width="1.8" fill="none"/></svg>Pinecove Benefits</div>
        </div>
      </div>
      <div class="photo" role="img" aria-label="Practitioner talking with a patient in the clinic" style="height:120px;margin-top:8px;background:linear-gradient(135deg,#eef2f6,var(--photo-b))"></div>
      <div class="photo" role="img" aria-label="Smiling clinic receptionist" style="height:148px;background:linear-gradient(160deg,#f4f6f8,#c9d6e2)"></div>
    </div>

    <div class="panel panel--prices">
      <div class="band">PRICES</div>
      <div class="photo" role="img" aria-label="Therapist treating a patient's shoulder" style="height:88px;background:linear-gradient(135deg,var(--photo-c),#aebfd0)"></div>
      <div class="prices">
        <div class="price-cols">
          <div class="price-group"><div class="heading-sm">Massage Therapy</div>
            <div class="price-row"><span>30 minutes</span><span>$60</span></div>
            <div class="price-row"><span>60 minutes</span><span>$95</span></div>
            <div class="price-row"><span>90 minutes</span><span>$135</span></div></div>
          <div class="price-group"><div class="heading-sm">Acupuncture</div>
            <div class="price-row"><span>Initial</span><span>$90</span></div>
            <div class="price-row"><span>Follow-up</span><span>$70</span></div></div>
          <div class="price-group"><div class="heading-sm">Chiropractic</div>
            <div class="price-row"><span>Initial</span><span>$85</span></div>
            <div class="price-row"><span>Follow-up</span><span>$55</span></div></div>
          <div class="price-group"><div class="heading-sm">Shockwave Therapy</div>
            <div class="price-row"><span>Per session</span><span>$75</span></div>
            <div class="price-row"><span>Package of 5</span><span>$325</span></div></div>
        </div>
        <div class="photo" role="img" aria-label="Therapist working on a patient's back" style="height:66px;margin:2px 0 6px;background:linear-gradient(135deg,#e3e9ef,#b3c3d3)"></div>
        <div class="price-cols">
          <div class="price-group"><div class="heading-sm">Manual Osteopathic Therapy</div>
            <div class="price-row"><span>Initial</span><span>$110</span></div>
            <div class="price-row"><span>Follow-up</span><span>$90</span></div></div>
          <div class="price-group"><div class="heading-sm">Pembrill Method</div>
            <div class="price-row"><span>Add-on</span><span>$20</span></div></div>
          <div class="price-group"><div class="heading-sm">Laser Therapy</div>
            <div class="price-row"><span>Per session</span><span>$45</span></div></div>
          <div class="price-group"><div class="heading-sm">Cupping Technique</div>
            <div class="price-row"><span>Add-on</span><span>$20</span></div></div>
        </div>
      </div>
    </div>
  </section>

</div>
</body>
</html>
```